Corvane semiconductor corporate presentation

We need a new template with some fresh design elements as we've just announced the acquisition of a new company. Similarly, the backend of the ppt is not set up correctly - and doesn't format properly when dropping in copied text. Attached is the powerpoint presentation/ template as it stands today.
Industry/Entity Type
It Company
Font styles to use
Other font styles liked:
- Arial
Look and feel
Each slider illustrates characteristics of the customer's brand and the style your logo design should communicate.

```html
<!DOCTYPE html>
<html lang="en">
<head>
<meta charset="utf-8">
<title>Corvane semiconductor – Corporate Presentation</title>
<link href="https://fonts.googleapis.com/css2?family=Roboto+Slab:wght@300;400;700&family=Arimo:wght@400;700&display=swap" rel="stylesheet">
<style>
:root{
  --blue:#1ba1da;
  --teal:#1f6e95;
  --green:#8cc63f;
  --lime:#b7d433;
  --leaf:#3dbb4e;
  --navy:#2c3a4e;
  --ink:#222;
  --grey:#8a8f96;
  --panel:#efefef;
  --bg:#c9cacb;
}
*{box-sizing:border-box;margin:0;padding:0}
html,body{width:1200px;height:915px;overflow:hidden;background:var(--bg)}
body{font-family:Arimo,Arial,sans-serif;color:var(--ink);position:relative}
.slide{position:absolute;width:391px;height:221px;background:#fff;overflow:hidden}
.abs{position:absolute}
.title{position:absolute;right:38px;top:7px;font-family:"Roboto Slab",Georgia,serif;font-weight:700;font-size:13px;line-height:16px;color:var(--ink);white-space:nowrap;z-index:2}
.title em{font-style:normal;color:var(--blue)}
.num{position:absolute;right:12px;top:4px;width:14px;height:17px;background:var(--blue);color:#fff;font-size:5px;text-align:center;line-height:17px;z-index:2}
.foot-line{position:absolute;left:0;right:60px;bottom:10px;height:1px;background:#444}
.brand{position:absolute;right:10px;bottom:4px;font-size:11px;color:var(--blue);display:flex;align-items:center;gap:2px;font-family:Arimo,Arial,sans-serif}
.brand i{display:block;width:8px;height:8px;border-radius:50%;background:var(--blue)}
.intro{position:absolute;right:38px;top:32px;width:300px;text-align:right;font-size:5.6px;color:#555;line-height:1.35}
.intro b{color:#111}
.tiny{font-size:4.3px;color:#777;line-height:1.35}
.tile{position:absolute;display:flex;align-items:center;justify-content:center}
.tile svg{width:45%;height:45%}
.lbl{position:absolute;font-size:5px;color:#444;text-align:center}
.bullets{list-style:none}
.bullets li{position:relative;padding-left:8px}
.bullets li:before{content:"";position:absolute;left:1px;top:.45em;width:3px;height:3px;border-radius:50%;background:var(--blue)}
.tri li:before{border-radius:0;width:0;height:0;background:none;border-left:3px solid #222;border-top:2px solid transparent;border-bottom:2px solid transparent}
.photo{position:relative;height:60px;background:linear-gradient(160deg,#2b6f9d,#24496a)}
.photo span{position:absolute;right:3px;top:2px;font-size:5px;color:#fff}
</style>
</head>
<body>

<!-- 1 Cover -->
<section class="slide" style="left:6px;top:6px">
  <div class="abs" style="left:21px;top:28px;font-size:17px;color:var(--blue);display:flex;align-items:center;gap:3px"><i style="display:block;width:11px;height:11px;border-radius:50%;background:var(--blue)"></i>corvane</div>
  <div class="abs" style="left:37px;top:47px;font-size:3.5px;color:var(--blue)">SEMICONDUCTOR</div>
  <div class="abs" style="left:22px;top:60px;font-family:'Roboto Slab',serif;font-weight:300;font-size:16.5px;color:#777">CORPORATE</div>
  <div class="abs" style="left:22px;top:77px;font-family:'Roboto Slab',serif;font-weight:700;font-size:16.5px;color:#666">PRESENTATION</div>
  <div class="abs" style="left:22px;top:97px;width:138px;height:2px;background:var(--blue)"></div>
  <div class="abs" style="left:22px;top:106px;width:150px;font-size:6px;color:#999;line-height:1.45">Maecenas venenatis faucibus lectus, quis iaculis orci tincidunt auctor.</div>
  <div class="abs" style="left:22px;top:134px;font-size:7.2px;color:#555">Presented by : <span style="color:var(--teal)">Jane Marlow</span></div>
  <div class="abs" style="left:22px;top:149px;width:151px;height:13px;background:var(--navy);color:#fff;font-size:6.5px;text-align:center;line-height:13px">Oct 2017</div>
  <div class="abs tiny" style="left:22px;top:178px;display:flex;gap:14px;align-items:center">
    <span style="display:flex;align-items:center;gap:3px"><i style="width:8px;height:8px;border-radius:50%;background:var(--green);display:block"></i>info@corvane.com</span>
    <span style="display:flex;align-items:center;gap:3px"><i style="width:8px;height:8px;border-radius:50%;background:var(--blue);display:block"></i>1-555-0142</span>
  </div>
  <div class="abs" style="left:0;right:0;bottom:10px;height:1px;background:#333"></div>
  <svg class="abs" style="left:0;top:0" width="391" height="221" viewBox="0 0 391 221">
    <defs>
      <linearGradient id="stripe" x1="0" y1="0" x2="0" y2="1"><stop offset="0" stop-color="#1ba1da"/><stop offset="1" stop-color="#8cc63f"/></linearGradient>
      <linearGradient id="coverPhoto" x1="0" y1="0" x2="1" y2="1"><stop offset="0" stop-color="#5b7f9c"/><stop offset="1" stop-color="#2d5a85"/></linearGradient>
    </defs>
    <polygon points="222,221 260,60 291,221" fill="#2c3a4e"/>
    <polygon points="270,0 310,0 252,150 236,150" fill="url(#stripe)"/>
    <polygon points="310,0 391,0 391,221 291,221 252,150" fill="url(#coverPhoto)" role="img" aria-label="Photo of a young woman in glasses reading her phone while holding a coffee cup"/>
  </svg>
</section>

<!-- 2 Agenda -->
<section class="slide" style="left:405px;top:6px">
  <div class="title">List of <em>Agenda</em></div><div class="num">2</div>
  <div class="intro"><b>Contrary to popular belief,</b> Lorem Ipsum is not simply random text. It has roots in a piece of classical Latin literature from 45 BC.</div>
  <div class="abs" style="left:33px;top:60px;width:334px;height:127px;background:var(--panel);border:1px solid #ddd"></div>
  <div class="abs" style="left:60px;top:70px;width:290px;display:grid;grid-template-columns:repeat(3,1fr);row-gap:28px;column-gap:12px">
    <div><div style="display:flex"><span style="background:#555;color:#ddd;font-size:5px;padding:2px 6px 2px 4px">01.</span><span style="width:0;border-left:6px solid var(--blue);border-top:5px solid transparent;border-bottom:5px solid transparent"></span></div><p class="tiny" style="margin-top:6px">Contrary to popular belief, Lorem Ipsum is not simply random text.</p></div>
    <div><div style="display:flex"><span style="background:#555;color:#ddd;font-size:5px;padding:2px 6px 2px 4px">02.</span><span style="width:0;border-left:6px solid var(--leaf);border-top:5px solid transparent;border-bottom:5px solid transparent"></span></div><p class="tiny" style="margin-top:6px">Contrary to popular belief, Lorem Ipsum is not simply random text.</p></div>
    <div><div style="display:flex"><span style="background:#555;color:#ddd;font-size:5px;padding:2px 6px 2px 4px">03.</span><span style="width:0;border-left:6px solid var(--lime);border-top:5px solid transparent;border-bottom:5px solid transparent"></span></div><p class="tiny" style="margin-top:6px">Contrary to popular belief, Lorem Ipsum is not simply random text.</p></div>
    <div><div style="display:flex"><span style="background:#555;color:#ddd;font-size:5px;padding:2px 6px 2px 4px">04.</span><span style="width:0;border-left:6px solid var(--green);border-top:5px solid transparent;border-bottom:5px solid transparent"></span></div><p class="tiny" style="margin-top:6px">Contrary to popular belief, Lorem Ipsum is not simply random text.</p></div>
    <div><div style="display:flex"><span style="background:#555;color:#ddd;font-size:5px;padding:2px 6px 2px 4px">05.</span><span style="width:0;border-left:6px solid var(--leaf);border-top:5px solid transparent;border-bottom:5px solid transparent"></span></div><p class="tiny" style="margin-top:6px">Contrary to popular belief, Lorem Ipsum is not simply random text.</p></div>
    <div><div style="display:flex"><span style="background:#555;color:#ddd;font-size:5px;padding:2px 6px 2px 4px">06.</span><span style="width:0;border-left:6px solid var(--blue);border-top:5px solid transparent;border-bottom:5px solid transparent"></span></div><p class="tiny" style="margin-top:6px">Contrary to popular belief, Lorem Ipsum is not simply random text.</p></div>
  </div>
  <div class="foot-line"></div><div class="brand"><i></i>corvane</div>
</section>

<!-- 3 At a glance -->
<section class="slide" style="left:803px;top:6px">
  <div class="title">Corvane at <em>a Glance</em></div><div class="num">3</div>
  <ul class="bullets tri abs" style="left:26px;top:28px;font-size:5.3px;color:#333"><li>Accelerated Growth (US $Million)</li></ul>
  <ul class="bullets tri abs" style="left:222px;top:28px;font-size:5.3px;color:#333"><li>Business Segments</li></ul>
  <svg class="abs" style="left:40px;top:42px" width="160" height="85" viewBox="0 0 160 85">
    <line x1="5" y1="60" x2="140" y2="8" stroke="#8cc63f" stroke-width="1.5"/>
    <rect x="26" y="8" width="50" height="14" fill="#2c3a4e"/><polygon points="45,22 52,22 48,27" fill="#2c3a4e"/>
    <text x="51" y="18" fill="#fff" font-size="6.5" text-anchor="middle">34% CAGR</text>
    <g fill="#1ba1da">
      <rect x="2" y="72" width="5" height="4" fill="#e0382a"/><rect x="16" y="70" width="5" height="6"/><rect x="30" y="68" width="5" height="8"/><rect x="44" y="65" width="5" height="11"/><rect x="58" y="55" width="5" height="21"/><rect x="72" y="45" width="5" height="31"/><rect x="86" y="40" width="5" height="36"/><rect x="100" y="36" width="5" height="40"/><rect x="114" y="22" width="5" height="54"/><rect x="128" y="28" width="5" height="48" fill="#2c3a4e"/>
    </g>
    <g font-size="3.6" fill="#555" text-anchor="middle">
      <text x="4" y="69">87</text><text x="18" y="67">162</text><text x="32" y="65">218</text><text x="46" y="62">296</text><text x="60" y="52">527</text><text x="74" y="42">774</text><text x="88" y="37">903</text><text x="102" y="33">1156</text><text x="116" y="19">1355</text><text x="130" y="25">1198</text>
      <text x="4" y="82">2007</text><text x="18" y="82">2008</text><text x="32" y="82">2009</text><text x="46" y="82">2010</text><text x="60" y="82">2011</text><text x="74" y="82">2012</text><text x="88" y="82">2013</text><text x="102" y="82">2014</text><text x="116" y="82">2015</text><text x="130" y="82">2016</text>
    </g>
  </svg>
  <div class="tile" style="left:219px;top:50px;width:48px;height:48px;background:var(--blue)"><svg viewBox="0 0 24 24"><rect x="7" y="3" width="10" height="18" rx="1.5" fill="none" stroke="#fff" stroke-width="1.6"/></svg></div>
  <div class="tile" style="left:276px;top:50px;width:48px;height:48px;background:var(--blue)"><svg viewBox="0 0 24 24"><polygon points="13,2 6,13 11,13 9,22 18,10 13,10" fill="#fff"/></svg></div>
  <div class="tile" style="left:333px;top:50px;width:48px;height:48px;background:var(--blue)"><svg viewBox="0 0 24 24"><path d="M7 4v16M17 4v6c0 3-10 3-10 7" fill="none" stroke="#fff" stroke-width="1.8"/></svg></div>
  <div class="lbl" style="left:219px;top:104px;width:48px">Mobile Systems</div>
  <div class="lbl" style="left:276px;top:104px;width:48px">Power Conversion</div>
  <div class="lbl" style="left:333px;top:104px;width:48px">Connectivity</div>
  <div class="abs" style="left:0;right:0;top:126px;height:9px;background:linear-gradient(90deg,var(--blue),var(--green));color:#fff;font-size:4.8px;text-align:center;line-height:9px">Company Overview</div>
  <ul class="bullets abs tiny" style="left:26px;top:143px;width:150px">
    <li>Fabless supplier of highly integrated mixed-signal ICs for mobile, wearables, IoT and smart home devices</li>
    <li>Manufacturing: fabless model with production, assembly and packaging fully outsourced</li>
    <li>Employees: c. 1,880 (75% engineers)</li>
    <li>One of the fastest growing global semiconductor companies</li>
  </ul>
  <ul class="bullets abs tiny" style="left:222px;top:143px;width:160px">
    <li>Best-in-class mobile PMIC platform with broad IP portfolio</li>
    <li>New technologies for RF wireless charging and GaN</li>
    <li>#1 PMIC market share for smartphones and tablets</li>
    <li>#1 in rapid charging for smartphone adapters</li>
    <li>Industry largest custom mixed-signal design team</li>
    <li>Track record of solid execution with strong revenue growth and cash generation</li>
  </ul>
  <div class="foot-line"></div><div class="brand"><i></i>corvane</div>
</section>

<!-- 4 Technology leadership -->
<section class="slide" style="left:6px;top:233px">
  <div class="title">Technology <em>Leadership</em></div><div class="num">4</div>
  <div class="intro"><b>Contrary to popular belief,</b> Lorem Ipsum is not simply random text. It has roots in a piece of classical Latin literature from 45 BC.</div>
  <div class="abs" style="left:0;right:0;top:64px;height:99px;background:linear-gradient(100deg,#1b8cc4 0%,#27a3c8 45%,#8cc63f 100%)"></div>
  <ul class="bullets abs" style="left:50px;top:94px;font-size:5.9px;color:#fff;line-height:1.85">
    <li>Leadership portfolio in power savings technologies</li>
    <li>Best-in-class PMIC with broad IP portfolios #1 PMIC market share for smartphones and tablets</li>
    <li>#2 LinkWave low-energy market share, ~100M units shipped with industry’s lowest power</li>
    <li>#1 in SwiftCharge (fast charging) market share for power adapters</li>
    <li>Industry leading RF wireless charging and GaN offering</li>
  </ul>
  <div class="foot-line"></div><div class="brand"><i></i>corvane</div>
</section>

<!-- 5 Product portfolio -->
<section class="slide" style="left:405px;top:233px">
  <div class="title"><em>Diverse</em> Product Portfolio</div><div class="num">5</div>
  <div class="abs" style="right:38px;top:31px;font-size:6px;color:#555">Powering efficient, smart connected devices</div>
  <div class="lbl" style="left:76px;top:56px;width:55px">Power<br>Management</div>
  <div class="lbl" style="left:139px;top:56px;width:55px">Wireless<br>Connectivity</div>
  <div class="lbl" style="left:202px;top:56px;width:55px">Audio</div>
  <div class="lbl" style="left:265px;top:56px;width:55px">Power Conversion</div>
  <div class="lbl" style="left:328px;top:56px;width:55px">Lighting</div>
  <div class="abs" style="left:76px;top:69px;width:307px;border-top:1px solid #bbb"></div>
  <div class="tile" style="left:76px;top:74px;width:55px;height:53px;background:var(--teal)"><svg viewBox="0 0 24 24"><polygon points="13,3 8,13 11,13 10,21 16,10 13,10" fill="#fff"/></svg></div>
  <div class="tile" style="left:139px;top:74px;width:55px;height:53px;background:var(--blue)"><svg viewBox="0 0 24 24"><path d="M4 10a11 11 0 0116 0M7 13a7 7 0 0110 0M10 16a3 3 0 014 0" fill="none" stroke="#fff" stroke-width="1.8"/><circle cx="12" cy="19" r="1.4" fill="#fff"/></svg></div>
  <div class="tile" style="left:202px;top:74px;width:55px;height:53px;background:#27a8dc"><svg viewBox="0 0 24 24"><polygon points="4,9 8,9 13,5 13,19 8,15 4,15" fill="#fff"/><path d="M16 9a4 4 0 010 6M18 7a7 7 0 010 10" fill="none" stroke="#fff" stroke-width="1.5"/></svg></div>
  <div class="tile" style="left:265px;top:74px;width:55px;height:53px;background:var(--leaf)"><svg viewBox="0 0 24 24"><path d="M8 7a7 7 0 108 0" fill="none" stroke="#fff" stroke-width="2"/><line x1="12" y1="4" x2="12" y2="12" stroke="#fff" stroke-width="2"/></svg></div>
  <div class="tile" style="left:328px;top:74px;width:55px;height:53px;background:var(--lime)"><svg viewBox="0 0 24 24"><circle cx="12" cy="10" r="5.5" fill="none" stroke="#fff" stroke-width="1.6"/><rect x="10" y="16" width="4" height="4" fill="#fff"/></svg></div>
  <div class="abs" style="left:32px;top:138px;font-size:6px;color:#333">Products</div>
  <div class="abs tiny" style="left:80px;top:137px;width:300px;display:grid;grid-template-columns:repeat(5,1fr);gap:8px">
    <span>PMICs, Chargers Wireless Charging</span><span>LinkWave DECT</span><span>Codecs, Amplifiers, Processors</span><span>AC/DC Converters</span><span>LED Drivers</span>
  </div>
  <div class="abs" style="left:12px;right:12px;top:150px;height:4px;background:var(--blue)"></div>
  <div class="abs" style="left:22px;top:163px;font-size:6px;color:var(--blue)">Corvane Values</div>
  <div class="abs tiny" style="left:80px;top:159px;width:300px;display:grid;grid-template-columns:repeat(5,1fr);gap:8px;color:var(--blue)">
    <span>Integration, Efficiency, Size, Flexibility</span><span>Performance &amp; Battery Life</span><span>Audio Quality &amp; Battery Life</span><span>Power Efficiency, Size, BOM Cost</span><span>Power Efficiency, Size, BOM Cost</span>
  </div>
  <div class="abs" style="left:12px;right:12px;top:180px;border-top:1px solid #ccc"></div>
  <div class="foot-line"></div><div class="brand"><i></i>corvane</div>
</section>

<!-- 6 Focused on growth -->
<section class="slide" style="left:803px;top:233px">
  <div class="num">6</div>
  <div class="abs" style="right:38px;top:34px;font-size:6.5px;color:#555">Lowest power solutions available</div>
  <div class="abs" style="left:10px;top:80px;width:118px;text-align:right;font-family:'Roboto Slab',serif;font-weight:700;font-size:12.5px;line-height:1.3;color:#444"><span style="color:var(--blue)">Focused</span><br><span style="color:var(--blue)">on</span> Growth<br>Markets and<br>Applications</div>
  <div class="tile" style="left:133px;top:51px;width:46px;height:46px;background:var(--teal)"><svg viewBox="0 0 24 24"><rect x="7" y="3" width="10" height="18" rx="1.5" fill="none" stroke="#fff" stroke-width="1.6"/></svg></div>
  <div class="tile" style="left:210px;top:51px;width:46px;height:46px;background:var(--blue)"><svg viewBox="0 0 24 24"><rect x="6" y="3" width="12" height="18" fill="none" stroke="#fff" stroke-width="1.5"/><path d="M9 7h2M13 7h2M9 11h2M13 11h2M9 15h2M13 15h2" stroke="#fff" stroke-width="1.4"/></svg></div>
  <div class="tile" style="left:287px;top:51px;width:46px;height:46px;background:#27a8dc"><svg viewBox="0 0 24 24"><rect x="5" y="4" width="14" height="13" rx="2" fill="none" stroke="#fff" stroke-width="1.6"/><line x1="5" y1="11" x2="19" y2="11" stroke="#fff" stroke-width="1.4"/><circle cx="8" cy="19" r="1.5" fill="#fff"/><circle cx="16" cy="19" r="1.5" fill="#fff"/></svg></div>
  <div class="lbl" style="left:128px;top:104px;width:56px">Smartphone</div>
  <div class="lbl" style="left:205px;top:104px;width:56px">Smart Building</div>
  <div class="lbl" style="left:282px;top:104px;width:56px">Automotive</div>
  <div class="tile" style="left:133px;top:128px;width:46px;height:46px;background:#8a8f96"><svg viewBox="0 0 24 24"><path d="M5 9h5V6a2 2 0 014 0v3h5v10H5z" fill="#fff"/></svg></div>
  <div class="tile" style="left:210px;top:128px;width:46px;height:46px;background:var(--lime)"><svg viewBox="0 0 24 24"><circle cx="12" cy="12" r="8" fill="none" stroke="#fff" stroke-width="1.8"/><polygon points="10,8 16,12 10,16" fill="#fff"/></svg></div>
  <div class="tile" style="left:287px;top:128px;width:46px;height:46px;background:var(--leaf)"><svg viewBox="0 0 24 24"><rect x="3" y="5" width="18" height="11" fill="none" stroke="#fff" stroke-width="1.6"/><path d="M9 20h6M12 16v4" stroke="#fff" stroke-width="1.6"/></svg></div>
  <div class="lbl" style="left:128px;top:181px;width:56px">Miscelleneous</div>
  <div class="lbl" style="left:205px;top:181px;width:56px">Smart Wear</div>
  <div class="lbl" style="left:282px;top:181px;width:56px">Smart TV</div>
  <div class="foot-line"></div><div class="brand"><i></i>corvane</div>
</section>

<!-- 7 At a glance R&D -->
<section class="slide" style="left:6px;top:460px">
  <div class="title">Corvane at <em>a Glance</em></div><div class="num">7</div>
  <ul class="bullets tri abs" style="left:26px;top:28px;font-size:5.3px;color:#333"><li>Sustained investment in R&amp;D for future growth</li></ul>
  <ul class="bullets tri abs" style="left:222px;top:28px;font-size:5.3px;color:#333"><li>Continued investment in new technologies</li></ul>
  <div class="abs" style="left:0;right:0;top:40px;border-top:1px solid #ddd"></div>
  <div class="abs" style="left:152px;top:47px;font-size:3.8px;color:#555">▪R&amp;D</div>
  <svg class="abs" style="left:25px;top:52px" width="170" height="70" viewBox="0 0 170 70">
    <rect x="22" y="13" width="24" height="47" fill="#1ba1da"/><rect x="75" y="11" width="24" height="49" fill="#1ba1da"/><rect x="128" y="7" width="24" height="53" fill="#1ba1da"/>
    <line x1="5" y1="60" x2="165" y2="60" stroke="#888" stroke-width=".5"/>
    <g font-size="5.5" fill="#fff" text-anchor="middle"><text x="34" y="38">213</text><text x="87" y="37">223</text><text x="140" y="35">241</text></g>
    <g font-size="4.5" fill="#444" text-anchor="middle"><text x="34" y="67">FY 2014</text><text x="87" y="67">FY 2015</text><text x="140" y="67">FY 2016</text></g>
  </svg>
  <div class="abs" role="img" aria-label="Block schematic of the VoltGaN half-bridge power stage" style="left:215px;top:52px;width:76px;height:65px;border:1px solid #222;background:linear-gradient(135deg,#fafafa,#e6e6e6)"></div>
  <div class="abs" role="img" aria-label="Photo of a GaN semiconductor wafer" style="left:307px;top:50px;width:76px;height:68px;background:linear-gradient(135deg,#d8cc8e,#b5a25a)"></div>
  <div class="abs" style="left:0;right:0;top:126px;height:6px;background:linear-gradient(90deg,var(--blue),var(--green))"></div>
  <div class="abs" style="left:12px;top:139px;width:375px;display:flex;align-items:center;gap:4px;font-size:6px;color:#333">
    <span style="flex:1;height:1px;background:#f0b400"></span><span>~ 900 Patents Issued</span><span style="flex:1;height:1px;background:#f0b400"></span>
  </div>
  <div class="abs" style="left:12px;top:149px;width:375px;height:35px;display:flex;font-size:5.5px;color:#fff;text-align:center;line-height:35px">
    <div style="width:161px;background:#1ba1da;border-right:1px solid #fff">PIMC</div>
    <div style="width:107px;background:#27a8dc">POWER CONVERSION</div>
    <div style="width:18px;background:var(--leaf);writing-mode:vertical-rl;transform:rotate(180deg);line-height:18px;font-size:4.5px">Wireless</div>
    <div style="width:19px;background:var(--lime);writing-mode:vertical-rl;transform:rotate(180deg);line-height:19px;font-size:4.5px">Audio</div>
    <div style="flex:1;background:var(--teal)">PACKAGING &amp; SW</div>
  </div>
  <div class="foot-line"></div><div class="brand"><i></i>corvane</div>
</section>

<!-- 8 Corporate structure -->
<section class="slide" style="left:405px;top:460px">
  <div class="title">Corporate <em>Structure</em></div><div class="num">8</div>
  <div class="abs" style="right:38px;top:26px;font-size:6.5px;color:#555">≈1880 Employees Today &nbsp;&gt; 75% Engineering</div>
  <ul class="bullets tri abs" style="left:26px;top:39px;font-size:5.3px;color:#333"><li>Sustained investment in R&amp;D for future growth</li></ul>
  <ul class="bullets tri abs" style="left:222px;top:39px;font-size:5.3px;color:#333"><li>Continued investment in new technologies</li></ul>
  <svg class="abs" style="left:40px;top:53px" width="62" height="62" viewBox="0 0 42 42" role="img" aria-label="Employee distribution pie chart">
    <path d="M21 21 L21 1 A20 20 0 1 1 1.6 25.9 Z" fill="#1f6e95"/>
    <path d="M21 21 L1.6 25.9 A20 20 0 0 1 5 9 Z" fill="#27a8dc"/>
    <path d="M21 21 L5 9 A20 20 0 0 1 21 1 Z" fill="#3dbb4e"/>
    <g font-size="3.5" fill="#fff"><text x="26" y="26">69%</text><text x="6" y="20">15%</text><text x="12" y="10">16%</text></g>
  </svg>
  <div class="abs" style="left:133px;top:76px;font-size:4.5px;color:#333;line-height:1.9">▪Europe<br>▪US America<br>▪Asia</div>
  <ul class="bullets tri abs tiny" style="left:222px;top:54px;line-height:1.75;color:#444">
    <li>Engineering</li><li>Finance</li><li>HR</li><li>Corporate Development &amp; Strategy</li><li>Manufacturing, Operations &amp; Quality</li><li>Sales, Marketing</li><li>Advanced Technology</li>
  </ul>
  <div class="abs" style="left:0;right:0;top:118px;height:18px;background:var(--panel)"></div>
  <div class="abs tiny" style="left:88px;top:124px;color:#444">Distribution partners</div>
  <div class="abs" role="img" aria-label="Distribution partner badge" style="left:160px;top:123px;width:34px;height:8px;background:#d53a2f"></div>
  <div class="abs" role="img" aria-label="Distribution partner badge" style="left:203px;top:122px;width:20px;height:10px;border-radius:50%;background:#c8322a"></div>
  <div class="abs" role="img" aria-label="Distribution partner badge" style="left:232px;top:122px;width:28px;height:10px;background:#1f5ea8"></div>
  <div class="abs" style="left:22px;top:142px;font-size:5px;font-weight:700">R&amp;D Centers</div>
  <div class="abs" style="left:22px;top:148px;width:190px;border-top:1px solid #bbb"></div>
  <ul class="bullets abs tiny" style="left:22px;top:150px;width:90px;font-size:3.8px">
    <li>Ravensburg &amp; Kolding, Nordland</li><li>Eastbrook &amp; Holmfield, Aldermark</li><li>Veldhaven &amp; Marlo, Zeeland</li><li>Corinth &amp; Larne, Helios</li><li>Grauberg, Ostmark</li><li>Livara, Tessaly</li>
  </ul>
  <ul class="bullets abs tiny" style="left:114px;top:150px;width:95px;font-size:3.8px">
    <li>Kestra, Anatoly</li><li>Northbay &amp; Harlan, Eastland</li><li>Suwa, Hoshima</li><li>Linhai, Taoren</li><li>Mesa Vale, Redstone &amp; Arden, AZ</li>
  </ul>
  <div class="abs" style="left:216px;top:142px;font-size:5px;font-weight:700">Sales Offices</div>
  <div class="abs" style="left:216px;top:148px;width:160px;border-top:1px solid #bbb"></div>
  <ul class="bullets abs tiny" style="left:216px;top:150px;width:85px;font-size:3.8px">
    <li>Taoren, Linhai ROC</li><li>Hanrei, Koryo</li><li>Hoshima, Suwa</li><li>Qingshan, Baolin, Harbour City</li><li>Marina Bay</li>
  </ul>
  <ul class="bullets abs tiny" style="left:300px;top:150px;width:80px;font-size:3.8px">
    <li>Ravensburg, Nordland</li><li>Veldhaven, Zeeland</li><li>Santa Rosa, CA, US</li><li>Ravensburg, Nordland</li>
  </ul>
  <div class="foot-line"></div><div class="brand"><i></i>corvane</div>
</section>

<!-- 9 Executive team -->
<section class="slide" style="left:803px;top:460px">
  <div class="title">Executive <em>Team</em></div><div class="num">9</div>
  <div class="abs" style="left:20px;top:29px;font-size:4.2px;line-height:1.7;display:grid;grid-template-columns:8px 50px 118px 8px 42px 130px;color:#333">
    <span style="color:var(--blue)">01</span><span>Arden Vale</span><span style="color:#888">Chief Executive Officer</span><span style="color:var(--blue)">07</span><span>Owen Tan</span><span style="color:#888">SVP &amp; GM, Power Conversion Business Group</span>
    <span style="color:var(--blue)">02</span><span>Rohan Iyer</span><span style="color:#888">SVP, Engineering</span><span style="color:var(--blue)">08</span><span>Ciaran Doyle</span><span style="color:#888">SVP &amp; GM, Connectivity, Auto &amp; Industrial</span>
    <span style="color:var(--blue)">03</span><span>Luc Marchal</span><span style="color:#888">SVP, Asia</span><span style="color:var(--blue)">09</span><span>Neil Harper</span><span style="color:#888">SVP, HR</span>
    <span style="color:var(--blue)">04</span><span>Samir Haddad</span><span style="color:#888">SVP, Global Manufacturing Operations &amp; Quality</span><span style="color:var(--blue)">10</span><span>Ray Ortega</span><span style="color:#888">SVP, Worldwide Sales</span>
    <span style="color:var(--blue)">05</span><span>Karim Nassar</span><span style="color:#888">Chief Financial Officer</span><span style="color:var(--blue)">11</span><span>Miles Crane</span><span style="color:#888">SVP, General Counsel</span>
    <span style="color:var(--blue)">06</span><span>Jens Albers</span><span style="color:#888">SVP &amp; GM, Mobile Systems Business Group</span><span style="color:var(--blue)">12</span><span>Gareth Lowe</span><span style="color:#888">SVP, Corporate Development &amp; Strategy</span>
  </div>
  <div class="abs" style="left:20px;top:80px;width:365px;display:grid;grid-template-columns:repeat(6,1fr);gap:1px">
    <div class="photo" role="img" aria-label="Portrait of executive 01"><span>01</span></div>
    <div class="photo" role="img" aria-label="Portrait of executive 02"><span>02</span></div>
    <div class="photo" role="img" aria-label="Portrait of executive 03"><span>03</span></div>
    <div class="photo" role="img" aria-label="Portrait of executive 04"><span>04</span></div>
    <div class="photo" role="img" aria-label="Portrait of executive 05"><span>05</span></div>
    <div class="photo" role="img" aria-label="Portrait of executive 06"><span>06</span></div>
    <div class="photo" role="img" aria-label="Portrait of executive 07"><span>07</span></div>
    <div class="photo" role="img" aria-label="Portrait of executive 08"><span>08</span></div>
    <div class="photo" role="img" aria-label="Portrait of executive 09"><span>09</span></div>
    <div class="photo" role="img" aria-label="Portrait of executive 10"><span>10</span></div>
    <div class="photo" role="img" aria-label="Portrait of executive 11"><span>11</span></div>
    <div class="photo" role="img" aria-label="Portrait of executive 12"><span>12</span></div>
  </div>
  <div class="foot-line"></div><div class="brand"><i></i>corvane</div>
</section>

<!-- 10 Financial position -->
<section class="slide" style="left:6px;top:686px">
  <div class="title"><em>Strong</em> Financial Position</div><div class="num">10</div>
  <div class="abs" style="left:202px;top:27px;width:157px;text-align:right;font-size:6.8px;color:var(--blue);padding-bottom:3px;border-bottom:1px solid #333">2016 Revenue Breakdown</div>
  <svg class="abs" style="left:14px;top:50px" width="170" height="150" viewBox="0 0 170 150">
    <text x="80" y="9" font-size="5.5" fill="#555">Revenue ($Million)</text>
    <g font-size="4.5" fill="#666" text-anchor="end"><text x="28" y="22">1200</text><text x="28" y="81">600</text><text x="28" y="142">0</text></g>
    <line x1="34" y1="140" x2="165" y2="140" stroke="#999" stroke-width=".5"/>
    <line x1="34" y1="18" x2="34" y2="140" stroke="#999" stroke-width=".5"/>
    <rect x="38" y="132" width="54" height="8" fill="#1ba1da"/>
    <rect x="102" y="20" width="54" height="120" fill="#1ba1da"/>
    <g font-size="4.5" fill="#666" text-anchor="middle"><text x="65" y="148">2007</text><text x="129" y="148">2016</text></g>
  </svg>
  <div class="abs" style="left:220px;top:69px;font-size:4.5px;line-height:1.7;color:#333"><span style="color:var(--teal)">▪</span>Mobile Systems<br><span style="color:var(--lime)">▪</span>Power Conversion<br><span style="color:var(--leaf)">▪</span>Connectivity</div>
  <svg class="abs" style="left:280px;top:60px" width="68" height="68" viewBox="0 0 42 42" role="img" aria-label="Revenue breakdown donut chart">
    <circle cx="21" cy="21" r="15.9" fill="none" stroke="#1ba1da" stroke-width="8"/>
    <circle cx="21" cy="21" r="15.9" fill="none" stroke="#8cc63f" stroke-width="8" stroke-dasharray="11 89" transform="rotate(-90 21 21)"/>
    <circle cx="21" cy="21" r="15.9" fill="none" stroke="#b7d433" stroke-width="8" stroke-dasharray="7 93" stroke-dashoffset="7" transform="rotate(-90 21 21)"/>
    <g font-size="3.2" fill="#fff"><text x="22" y="7">11%</text><text x="26" y="37">82%</text></g>
  </svg>
  <ul class="bullets tri abs" style="left:216px;top:143px;width:160px;font-size:5.6px;color:#333;line-height:1.55">
    <li>$1.198 billion revenue for calendar year 2016</li>
    <li>$271 million revenue for Q1 2017, +12% YoY</li>
    <li>$723 million cash &amp; cash equivalents balance at 31 March 2017</li>
  </ul>
  <div class="foot-line"></div><div class="brand"><i></i>corvane</div>
</section>

<!-- 11 Pillars of strategy -->
<section class="slide" style="left:405px;top:686px">
  <div class="abs" style="left:0;right:0;top:26px;height:172px;background:var(--panel)"></div>
  <div class="title"><em>Pillars</em> of our Strategy</div><div class="num">11</div>
  <svg class="abs" style="left:86px;top:55px" width="22" height="22" viewBox="0 0 24 24"><rect x="5" y="5" width="14" height="14" fill="#222"/><rect x="8" y="8" width="8" height="8" fill="#fff"/><path d="M8 2v3M12 2v3M16 2v3M8 19v3M12 19v3M16 19v3M2 8h3M2 12h3M2 16h3M19 8h3M19 12h3M19 16h3" stroke="#222" stroke-width="1.4"/></svg>
  <svg class="abs" style="left:237px;top:55px" width="22" height="22" viewBox="0 0 24 24"><rect x="8" y="4" width="9" height="16" rx="1.5" fill="#222"/><path d="M5 12l4-3v6z" fill="#222"/></svg>
  <svg class="abs" style="left:306px;top:53px" width="24" height="24" viewBox="0 0 24 24"><circle cx="14" cy="12" r="5" fill="none" stroke="#222" stroke-width="2.5" stroke-dasharray="2 1.5"/><circle cx="14" cy="12" r="2" fill="#222"/><circle cx="6" cy="16" r="2" fill="#222"/><circle cx="8" cy="7" r="1.6" fill="#222"/></svg>
  <div class="abs" style="left:40px;top:82px;width:310px;display:grid;grid-template-columns:repeat(3,1fr);text-align:center;font-size:5.2px;color:#333;row-gap:2px">
    <span>TECHNOLOGY</span><span>ENTER NEW MARKETS</span><span>MANUFACTURING &amp; SUPPLY CHAIN</span>
    <span class="tiny" style="color:#555">Adding Corvane IP to expand Corvane portfolio</span><span class="tiny" style="color:#555">Leverage Corvane’s position in mobile, computing and IoT</span><span class="tiny" style="color:#555">Common manufacturing supply chain</span>
  </div>
  <svg class="abs" style="left:86px;top:128px" width="24" height="22" viewBox="0 0 24 24"><circle cx="7" cy="7" r="3" fill="#222"/><circle cx="17" cy="8" r="3" fill="#222"/><path d="M3 20v-7h8v7zM13 20v-6h8v6z" fill="#222"/></svg>
  <svg class="abs" style="left:236px;top:128px" width="24" height="22" viewBox="0 0 24 24"><path d="M4 9l5-5 6 2 5 1-1 6-4 2-2 6-4-4-1-4-4-1z" fill="#222"/></svg>
  <svg class="abs" style="left:306px;top:128px" width="24" height="22" viewBox="0 0 24 24"><path d="M2 10l5-5 5 3 5-3 5 5-9 9z" fill="#222"/><path d="M8 12l4 3 4-3" stroke="#fff" stroke-width="1" fill="none"/></svg>
  <div class="abs" style="left:40px;top:156px;width:310px;display:grid;grid-template-columns:repeat(3,1fr);text-align:center;font-size:5.2px;color:#333;row-gap:2px">
    <span>SALES CHANNEL</span><span>EXPANDS FOOTPRINT</span><span>CUSTOMER RELATIONSHIPS</span>
    <span class="tiny" style="color:#555">Combining sales and distribution channels</span><span class="tiny" style="color:#555">Increases opportunities in growing markets</span><span class="tiny" style="color:#555">Deepens existing key customer relationships and adds new customers</span>
  </div>
  <div class="brand"><i></i>corvane</div>
</section>

<!-- 12 Thank you -->
<section class="slide" style="left:803px;top:686px;background:linear-gradient(135deg,#1b9fd6 0%,#2fb3b0 45%,#9ecf3a 100%)">
  <div class="abs" style="left:131px;top:0;width:126px;height:221px;background:#fff"></div>
  <div class="abs" style="left:131px;width:126px;top:96px;display:flex;justify-content:center;align-items:center;gap:3px;font-size:15px;color:var(--blue)"><i style="display:block;width:10px;height:10px;border-radius:50%;background:var(--blue)"></i>corvane</div>
  <div class="abs" style="left:131px;width:126px;top:113px;text-align:center;font-size:3.5px;color:var(--blue)">SEMICONDUCTOR</div>
  <div class="abs" style="left:131px;width:126px;top:120px;text-align:center;font-family:'Roboto Slab',serif;font-weight:700;font-size:14px;color:#555">Thank You</div>
  <div class="abs" style="left:131px;width:126px;top:141px;text-align:center;font-size:5.2px;color:var(--blue)">Please contact us for more information</div>
  <div class="abs tiny" style="left:138px;top:162px;display:flex;gap:10px;align-items:center">
    <span style="display:flex;align-items:center;gap:3px"><i style="width:8px;height:8px;border-radius:50%;background:var(--green);display:block"></i>info@corvane.com</span>
    <span style="display:flex;align-items:center;gap:3px"><i style="width:8px;height:8px;border-radius:50%;background:var(--blue);display:block"></i>1-555-0142</span>
  </div>
</section>

</body>
</html>
```